Vintrell Power Point Presentation

We need our presentation designed. Our current presentation is inconsistent, too text heavy, and complicated. We want this to be clean, sleek, and impressive as our references attached are.

Our colors are blue, black, and white.
Our font is roboto.

```html
<!DOCTYPE html>
<html lang="en">
<head>
<meta charset="utf-8">
<title>Vintrell Media Kit 2021 – Slide Overview</title>
<link href="https://fonts.googleapis.com/css2?family=Roboto:ital,wght@0,300;0,400;0,500;0,700;1,400&family=Roboto+Condensed:ital,wght@0,700;1,400&display=swap" rel="stylesheet">
<style>
:root{
  --blue:#1183f5;
  --blue-deep:#0a6fd8;
  --ink:#1d1d1f;
  --grey:#6d6d72;
  --light:#eef0f2;
  --white:#ffffff;
  --stage:#2a2a2b;
}
*{box-sizing:border-box;margin:0;padding:0}
html,body{width:1200px;height:757px;overflow:hidden;background:var(--stage);font-family:"Roboto",sans-serif}
.canvas{position:relative;width:1200px;height:757px;background:linear-gradient(135deg,#333 0%,#252526 50%,#2e2e2f 100%)}
.slide{position:absolute;width:349px;height:196px;overflow:hidden;background:linear-gradient(135deg,#fafafa,#e9ebed);box-shadow:0 4px 12px rgba(0,0,0,.45)}
.slide--blue{background:var(--blue)}
.abs{position:absolute}
.footer{position:absolute;left:0;top:172px;width:318px;height:16px;background:var(--blue);color:var(--white)}
.footer .brand{position:absolute;left:12px;top:3px;font-size:7px;font-weight:500}
.footer .url{position:absolute;left:133px;top:3px;font-size:5.5px;letter-spacing:2px}
.footer-badge{position:absolute;left:322px;top:171px;width:18px;height:18px;border-radius:4px;background:var(--blue)}
.title{position:absolute;left:13px;font-size:10px;color:var(--grey);font-weight:300;line-height:1.2}
.title b{color:var(--blue);font-weight:500}
.card{position:absolute;border:1.3px solid var(--blue);border-radius:6px;background:rgba(255,255,255,.85)}
.card-head{font-size:8px;color:var(--grey);font-weight:300;padding:3px 0 0 6px;line-height:1.1}
.card-head b{color:var(--blue);font-weight:500}
.tiny{font-size:3.6px;color:var(--grey);text-align:center;line-height:1.2}
.dot{position:absolute;width:10px;height:10px;border-radius:50%;background:var(--blue)}
.photo{position:absolute}
.frame{position:absolute;border:2px solid var(--blue);border-radius:7px;background:rgba(255,255,255,.9);display:flex;align-items:center;justify-content:center;text-align:center;color:#7a7a7e;font-weight:300}
.stat{position:absolute;text-align:center;color:var(--blue);font-size:9px;font-weight:500;line-height:1}
.stat small{display:block;font-size:3.6px;color:var(--grey);font-weight:400;margin-top:1px}
.tile{position:absolute;width:34px;height:20px;border:1px solid var(--blue);border-radius:3px;background:var(--white);display:flex;align-items:center;justify-content:center;text-align:center;font-size:4.6px;font-weight:500;color:var(--ink);line-height:1.05}
.partner{font-size:4.6px;font-weight:700;color:var(--ink);text-align:center;line-height:1.7}
.bullets{position:absolute;list-style:none;font-size:5.2px;color:var(--grey);line-height:1.25}
.bullets li{position:relative;padding-left:9px}
.bullets li::before{content:"›";position:absolute;left:1px;top:-1px;color:var(--blue);font-size:7px}
.col-head{position:absolute;font-size:6px;color:var(--ink);border-bottom:.6px solid #aaa;padding-bottom:2px}
</style>
</head>
<body>
<main class="canvas">

  <!-- Slide 1: cover -->
  <section class="slide" style="left:57px;top:55px">
    <div class="abs" style="left:215px;top:0;width:134px;height:196px;background:var(--blue)"></div>
    <div class="photo" role="img" aria-label="Wall of screens showing travel and lifestyle imagery" style="left:150px;top:52px;width:175px;height:144px;border-radius:22px 22px 0 0;background:linear-gradient(135deg,#3b4f6b,#7d8e9e 40%,#c49a5a 70%,#2d3a2a)"></div>
    <div class="abs" style="left:16px;top:16px;width:16px;height:16px;border-radius:3px;background:var(--blue)"></div>
    <div class="abs" style="left:37px;top:11px;font-size:21px;font-weight:500;color:var(--blue)">Vintrell</div>
    <div class="abs" style="left:264px;top:35px;font-size:8px;font-weight:500;color:var(--white)">MEDIA KIT 2021</div>
    <div class="abs" style="left:16px;top:84px;font-family:'Roboto Condensed',sans-serif;font-weight:700;font-size:16px;color:var(--blue)">Indoor DOOH</div>
    <div class="abs" style="left:16px;top:100px;font-family:'Roboto Condensed',sans-serif;font-style:italic;font-size:15px;color:var(--blue)">Audiences at Scale</div>
    <div class="abs" style="left:41px;top:155px;padding:2px 5px;border-radius:3px;background:var(--blue);color:var(--white);font-size:5.5px">BUY ON VINTRELL</div>
    <div class="abs" style="left:40px;top:173px;font-size:5.5px;color:var(--blue)">E : info@vintrell.com</div>
  </section>

  <!-- Slide 2: why go indoor -->
  <section class="slide" style="left:428px;top:55px">
    <div class="photo" role="img" aria-label="Faded indoor venue with a mounted ad screen" style="left:180px;top:0;width:169px;height:196px;background:linear-gradient(180deg,#e0e2e4,#c8cbce 60%,#b7babd)"></div>
    <div class="title" style="top:15px;width:260px"><b>WHY GO INDOOR|</b> it's not just lockdowns ending - recent uptick has been driven by the unique effectiveness of indoor DOOH ad exposure.</div>
    <div class="card" style="left:13px;top:62px;width:54px;height:98px">
      <div class="card-head">It's <b>special...</b></div>
      <div class="dot" style="left:9px;top:20px"></div><div class="dot" style="left:36px;top:20px"></div>
      <div class="tiny abs" style="left:2px;top:32px;width:24px">Dwell time in minutes, not seconds</div>
      <div class="tiny abs" style="left:29px;top:32px;width:24px">Brand-safe</div>
      <div class="dot" style="left:9px;top:56px"></div><div class="dot" style="left:36px;top:56px"></div>
      <div class="tiny abs" style="left:2px;top:69px;width:24px">100% viewability by humans, not bots</div>
      <div class="tiny abs" style="left:29px;top:69px;width:24px">Not Skippable</div>
    </div>
    <div class="card" style="left:81px;top:62px;width:59px;height:98px">
      <div class="card-head">It's <b>powerful...</b></div>
      <div class="dot" style="left:24px;top:20px"></div>
      <div class="tiny abs" style="left:4px;top:32px;width:50px">Engaged impressions, consumer attention, means.</div>
      <div class="dot" style="left:24px;top:55px"></div>
      <div class="tiny abs" style="left:4px;top:68px;width:50px">...Indoor DOOH 2x more likely to be seen, recalled, than traditional OOH</div>
    </div>
    <div class="card" style="left:152px;top:62px;width:59px;height:98px">
      <div class="card-head">And it <b>works.</b></div>
      <div class="dot" style="left:24px;top:20px"></div>
      <div class="tiny abs" style="left:4px;top:32px;width:50px;color:var(--blue)">2x increase in reach if added to Omni-Channel campaigns</div>
    </div>
    <div class="footer"><span class="brand">Vintrell</span><span class="url">www.vintrell.com</span></div>
    <div class="footer-badge"></div>
  </section>

  <!-- Slide 3: statement -->
  <section class="slide slide--blue" style="left:798px;top:55px">
    <div class="abs" style="left:55px;top:73px;width:240px;height:65px;border:1.3px solid var(--white);border-radius:6px;display:flex;align-items:center;justify-content:center;text-align:center;color:var(--white);font-size:10.5px;font-weight:500;line-height:1.15;padding:0 6px">Vintrell offers advertisers easy, affordable access to North America's largest indoor DOOH network, containing diverse audience segments while captivated in indoor environments</div>
  </section>

  <!-- Slide 4: network -->
  <section class="slide" style="left:57px;top:283px">
    <div class="title" style="top:15px;width:240px;font-size:8px"><b>NETWORK |</b> Vintrell is your DOOH partner, connecting your partners and advertisers to a nation-wide network of premium, place-based screens.</div>
    <div class="card" style="left:13px;top:49px;width:128px;height:113px">
      <div class="abs" style="left:4px;top:6px;font-size:6px;color:var(--ink)">Our <b style="color:var(--blue);font-weight:500">nationwide</b> network.</div>
      <div class="photo" role="img" aria-label="Map of US screen locations" style="left:5px;top:20px;width:72px;height:38px;border-radius:3px;background:linear-gradient(135deg,#d7dbe0,#bfc6cf)"></div>
      <div class="photo" role="img" aria-label="Map of Canadian screen locations" style="left:5px;top:62px;width:72px;height:46px;border-radius:3px;background:linear-gradient(135deg,#dfe2e5,#c4c9cf)"></div>
      <div class="stat" style="left:90px;top:9px;width:34px">12B+<small>Impressions Annually</small></div>
      <div class="stat" style="left:90px;top:38px;width:34px">50+<small>DMA's</small></div>
      <div class="stat" style="left:84px;top:64px;width:42px">26,105+<small>Venues</small></div>
      <div class="stat" style="left:84px;top:90px;width:42px">31,594+<small>Screens</small></div>
    </div>
    <div class="card" style="left:150px;top:49px;width:183px;height:113px">
      <div class="abs" style="left:4px;top:4px;font-size:6px;color:var(--ink)">Our <b style="color:var(--blue);font-weight:500">premium</b> venue types.</div>
      <div class="stat" style="left:5px;top:17px;width:32px;font-size:7.5px">12000+<small>Retail screens</small></div>
      <div class="stat" style="left:5px;top:40px;width:32px;font-size:7.5px">16000+<small>Restobar screens</small></div>
      <div class="stat" style="left:5px;top:63px;width:32px;font-size:7.5px">2000+<small>Medical screens</small></div>
      <div class="stat" style="left:5px;top:89px;width:32px;font-size:7.5px">4000+<small>Grocery screens</small></div>
      <div class="photo" role="img" aria-label="Retail store screen" style="left:45px;top:30px;width:45px;height:40px;border-radius:8px;background:linear-gradient(135deg,#8a6a5a,#c7b9a8)"></div>
      <div class="photo" role="img" aria-label="Restobar screen" style="left:96px;top:18px;width:40px;height:32px;border-radius:8px;background:linear-gradient(135deg,#3c5a8a,#a0a8b5)"></div>
      <div class="photo" role="img" aria-label="Grocery venue screen" style="left:142px;top:24px;width:36px;height:32px;border-radius:8px;background:linear-gradient(135deg,#4d8a3a,#b8c97a)"></div>
      <div class="photo" role="img" aria-label="Medical clinic screen" style="left:83px;top:66px;width:52px;height:40px;border-radius:8px;background:linear-gradient(135deg,#d5d8db,#6c7075)"></div>
      <div class="photo" role="img" aria-label="Arena food court screen" style="left:138px;top:70px;width:40px;height:36px;border-radius:8px;background:linear-gradient(135deg,#8a5a2a,#d9a050)"></div>
      <div class="tiny abs" style="left:40px;top:85px;width:40px">Plus private airports, hockey arenas, records stores, and many more.</div>
    </div>
    <div class="footer"><span class="brand">Vintrell</span><span class="url">www.vintrell.com</span></div>
    <div class="footer-badge"></div>
  </section>

  <!-- Slide 5: how to buy -->
  <section class="slide" style="left:428px;top:283px">
    <div class="photo" role="img" aria-label="Blurred commuters walking through a concourse" style="left:220px;top:30px;width:129px;height:166px;background:linear-gradient(160deg,#dfe1e3,#c2c5c8 50%,#e4e6e8)"></div>
    <div class="title" style="top:12px;width:280px"><b>HOW TO BUY |</b> Vintrell's network and unique audiences are accessible however you buy your media.</div>
    <div class="card" style="left:13px;top:45px;width:63px;height:117px">
      <div class="card-head" style="font-size:9px"><b>Audiences...</b></div>
      <div class="dot" style="left:12px;top:22px"></div><div class="dot" style="left:40px;top:22px"></div>
      <div class="tiny abs" style="left:2px;top:46px;width:28px;font-size:4.4px">High net worth</div>
      <div class="tiny abs" style="left:30px;top:46px;width:30px;font-size:4.4px">Sports Fans</div>
      <div class="dot" style="left:12px;top:64px"></div>
      <div class="abs" style="left:33px;top:68px;width:26px;height:16px;border:.6px solid #999;border-radius:2px"></div>
      <div class="tiny abs" style="left:33px;top:71px;width:26px">And many more.</div>
      <div class="tiny abs" style="left:2px;top:84px;width:28px;font-size:4.4px">High dwell time</div>
    </div>
    <div class="card" style="left:88px;top:45px;width:70px;height:117px">
      <div class="card-head" style="font-size:8.5px">...you can buy<br><b>anywhere...</b></div>
      <div class="abs" style="left:4px;top:28px;width:62px">
        <div class="partner">Bidgrid &nbsp; Tradelane</div>
        <div class="partner">omnibu</div>
        <div class="partner">Movera</div>
        <div class="partner">Kestral</div>
        <div class="partner">Pinecast</div>
        <div class="partner">Combhub</div>
        <div class="partner">Beatline &nbsp; Veritel Media</div>
        <div class="partner">Adwyn</div>
      </div>
    </div>
    <div class="card" style="left:170px;top:45px;width:69px;height:117px">
      <div class="card-head" style="font-size:8.5px;text-align:center;padding-left:0">...however<br><b>you'd like.</b></div>
      <div class="dot" style="left:29px;top:29px"></div>
      <div class="tiny abs" style="left:4px;top:42px;width:61px">Direct Buying</div>
      <div class="dot" style="left:29px;top:56px"></div>
      <div class="tiny abs" style="left:4px;top:69px;width:61px">Open RTB</div>
      <div class="dot" style="left:29px;top:83px"></div>
      <div class="tiny abs" style="left:4px;top:96px;width:61px">Programmatic Guaranteed or PMP</div>
    </div>
    <div class="footer"><span class="brand">Vintrell</span><span class="url">www.vintrell.com</span></div>
    <div class="footer-badge"></div>
  </section>

  <!-- Slide 6: advertisers -->
  <section class="slide" style="left:798px;top:283px">
    <div class="abs" style="left:42px;top:10px;width:265px;height:18px;border:1.2px solid var(--blue);border-radius:5px;font-size:10px;font-weight:300;color:var(--grey);text-align:center;line-height:16px"><b style="color:var(--blue);font-weight:500">ADVERTISERS |</b> Brands that buy on our network.</div>
    <div class="tile" style="left:77px;top:43px">Norvale Bank</div>
    <div class="tile" style="left:130px;top:43px">Maison Liré</div>
    <div class="tile" style="left:184px;top:43px">Starglen</div>
    <div class="tile" style="left:237px;top:43px">Porchly</div>
    <div class="tile" style="left:77px;top:76px">Harlow Motors</div>
    <div class="tile" style="left:130px;top:76px">Northland</div>
    <div class="tile" style="left:184px;top:76px">Flatnest</div>
    <div class="tile" style="left:237px;top:76px">Crunchos</div>
    <div class="tile" style="left:77px;top:108px">Paylink</div>
    <div class="tile" style="left:130px;top:108px">Burgerton</div>
    <div class="tile" style="left:184px;top:108px">Puckline</div>
    <div class="tile" style="left:237px;top:108px">Playwick</div>
    <div class="tile" style="left:77px;top:141px">Vaucrest</div>
    <div class="tile" style="left:130px;top:141px">Tunefield</div>
    <div class="tile" style="left:184px;top:141px">Hoagio</div>
    <div class="tile" style="left:237px;top:141px">Fizzwave</div>
    <div class="footer"><span class="brand">Vintrell</span><span class="url">www.vintrell.com</span></div>
    <div class="footer-badge"></div>
  </section>

  <!-- Slide 7: key takeaways -->
  <section class="slide" style="left:57px;top:513px">
    <div class="abs" style="left:14px;top:10px;font-size:15px;font-weight:300;color:var(--grey)"><b style="color:var(--blue);font-weight:500">VINTRELL |</b> Key Takeaways.</div>
    <div class="abs" style="left:14px;top:36px;width:155px;font-size:9px;color:var(--ink);font-weight:300;border-bottom:.6px solid #999;padding-bottom:2px">Vintrell is:</div>
    <ul class="bullets" style="left:14px;top:55px;width:160px">
      <li style="margin-bottom:15px">North America's largest and fastest growing indoor DOOH screen network</li>
      <li style="margin-bottom:15px">Powerful enough to capture the attention of nationwide audiences at scale, specific enough to provide access to diverse audience segments</li>
      <li style="margin-bottom:15px">Programmatically-accessible, ensuring cost-efficiency, transparency and real-time optimizations</li>
      <li>Flexible enough to get any DOOH campaign or integration up and running quickly and without issue</li>
    </ul>
    <div class="frame" style="left:190px;top:68px;width:136px;height:87px;font-size:12px;line-height:1.15">The Right Time.<br>The Right Message.<br>The Right Audience.</div>
    <div class="footer"><span class="brand">Vintrell</span><span class="url">www.vintrell.com</span></div>
    <div class="footer-badge"></div>
  </section>

  <!-- Slide 8: media formats -->
  <section class="slide" style="left:428px;top:513px">
    <div class="abs" style="left:14px;top:9px;font-size:14px;font-weight:300;color:var(--grey)"><b style="color:var(--blue);font-weight:500">DIGITAL MEDIA FORMATS |</b> Specifications.</div>
    <div class="col-head" style="left:14px;top:33px;width:60px">Network</div>
    <div class="col-head" style="left:89px;top:33px;width:63px">Content Specifications</div>
    <div class="col-head" style="left:171px;top:33px;width:84px">Ad Content Play Suggestions</div>
    <ul class="bullets" style="left:14px;top:46px;width:64px;font-size:4.8px">
      <li style="margin-bottom:6px">Indoor, 32 –73" Screens</li>
      <li style="margin-bottom:6px">Full Screen Take Over</li>
      <li style="margin-bottom:6px">Sold programmatically</li>
      <li style="margin-bottom:6px">No Blacklisted Advertisers</li>
      <li>Approval Upon Venue Review</li>
    </ul>
    <ul class="bullets" style="left:89px;top:46px;width:72px;font-size:4.8px">
      <li style="margin-bottom:6px">1920 pixels (w) x 1080 pixels (h) 16:9</li>
      <li style="margin-bottom:6px">1080 pixels (w) x 1920 pixels (h) 9:16</li>
      <li style="margin-bottom:6px">Static: PNG, RGB, encoded .JPG or H.264</li>
      <li style="margin-bottom:6px">Video: .MP$ / encoded .MOV</li>
      <li>Will repurpose TV spots, banner ads; transcode ill-fitting static creatives</li>
    </ul>
    <ul class="bullets" style="left:171px;top:46px;width:60px;font-size:4.8px">
      <li style="margin-bottom:6px">15 second</li>
      <li style="margin-bottom:6px">30 second</li>
      <li>60 second</li>
    </ul>
    <div class="frame" style="left:198px;top:80px;width:128px;height:82px;font-size:11px;line-height:1.18">The Right Time.<br>The Right Message.<br>The Right Audience.</div>
    <div class="footer"><span class="brand">Vintrell</span><span class="url">www.vintrell.com</span></div>
    <div class="footer-badge"></div>
  </section>

  <!-- Slide 9: thank you -->
  <section class="slide slide--blue" style="left:798px;top:513px">
    <div class="abs" style="left:86px;top:50px;width:177px;height:112px;border:2px solid var(--white);border-radius:8px"></div>
    <div class="abs" style="left:129px;top:72px;width:13px;height:13px;border-radius:2px;background:var(--white)"></div>
    <div class="abs" style="left:146px;top:67px;font-size:17px;font-weight:500;color:var(--white)">Vintrell</div>
    <div class="abs" style="left:86px;top:96px;width:177px;text-align:center;font-size:24px;font-weight:500;color:var(--white)">THANK YOU</div>
    <div class="abs" style="left:86px;top:139px;width:177px;text-align:center;font-size:5.5px;letter-spacing:2px;color:var(--white)">www.vintrell.com</div>
  </section>

</main>
</body>
</html>
```